Marwick Brewing Co Menu Design

I have an exisiting restaurant called Marwick Brewing Co. We have an official logo and an existing menu. We need something more professional and vibrant. We are a great little brewpub and need our menu to reflect the same.
Updates

I have added our existing menu that has our logo on first page. Please use and insert menu items and pricing. Thank you for all your help! I really need a great look... also our web site is marwickbrewingco.comĀ  that may help as well

I have been trying to uplaod pictures for the menu design today but for some reason I can not get them to upload on this site. Will keep trying and hope to have some posted soon.

I have submitted pictures to sketch harbor web administration and they will be posting to my project shortly.

All pictures have been posted for menu design. Thanks!

Industry/Entity Type

Restaurant

Requirements
Must have
• Great layout with pictures!!! Need it to be eye catching with current menu items and pricing. Needs to be a funtional format so I can easily changed to add or delete items as needed. I am looking for a one page menu that is 8 1/2 x 14 with front and back side print that will be placed in a clear menu cover.

```html
<!DOCTYPE html>
<html lang="en">
<head>
<meta charset="utf-8">
<title>Marwick Brewing Co – Lunch Menu</title>
<link rel="stylesheet" href="https://fonts.googleapis.com/css2?family=Arimo:wght@400;700&family=Cinzel:wght@700&display=swap">
<style>
  :root {
    --page-bg: #b8cde5;
    --frame: #e0762b;
    --ink: #1b1b1b;
    --heading: #e8781e;
    --heading-edge: #a3440c;
    --alert: #e8201c;
    --pizza-a: #e7c9a1;
    --pizza-b: #a24a2c;
    --sandwich-a: #d9b48a;
    --sandwich-b: #6e3a2a;
  }
  * { margin: 0; padding: 0; box-sizing: border-box; }
  html, body { width: 902px; height: 1200px; overflow: hidden; }
  body {
    background: var(--page-bg);
    font-family: "Arimo", Arial, sans-serif;
    color: var(--ink);
    position: relative;
  }
  .frame {
    position: absolute; left: 37px; top: 37px; width: 852px; height: 1126px;
    border: 3px solid var(--frame);
  }
  .frame-inner {
    position: absolute; left: 44px; top: 44px; width: 838px; height: 1112px;
    border: 1.5px solid var(--frame);
  }
  .item { position: absolute; left: 55px; width: 680px; }
  .item-name { font-weight: 700; font-size: 13.5px; line-height: 18px; text-transform: uppercase; }
  .item-desc { font-size: 12px; line-height: 19px; letter-spacing: -0.1px; }
  .item-desc strong { font-size: 13px; }
  .price { position: absolute; font-size: 12px; font-weight: 700; }
  .section-title {
    position: absolute; left: 0; width: 902px; text-align: center;
    font-family: "Cinzel", "Times New Roman", serif; font-weight: 700;
    font-size: 19px; color: var(--heading); letter-spacing: 0.5px;
    -webkit-text-stroke: 0.6px var(--heading-edge);
  }
  .section-note {
    position: absolute; left: 0; width: 902px; text-align: center;
    color: var(--alert); font-weight: 700;
  }
  .photo { position: absolute; border-radius: 4px; }
  .photo-pizza { left: 720px; top: 360px; width: 140px; height: 138px;
    background: radial-gradient(circle at 50% 50%, var(--pizza-a), var(--pizza-b) 80%, var(--page-bg) 100%); }
  .photo-sandwich { left: 746px; top: 930px; width: 120px; height: 76px;
    background: radial-gradient(ellipse at 50% 50%, var(--sandwich-a), var(--sandwich-b) 75%, var(--page-bg) 100%); }
</style>
</head>
<body>
  <div class="frame"></div>
  <div class="frame-inner"></div>

  <div class="item" style="top:74px">
    <div class="item-name">Albacore Melt:</div>
    <div class="item-desc">Made with celery, onion, dill and a “pinch” of cayenne for some kick.<br>Served with lettuce, tomato and Swiss cheese on Bavarian rye bread …</div>
    <span class="price" style="left:592px;top:37px">$8.95</span>
  </div>

  <div class="item" style="top:141px">
    <div class="item-name">Beef Short Rib:</div>
    <div class="item-desc"><strong>Slow roasted </strong>beef short rib dipped in veal au jus served on a French baguette with sweet potato fries …</div>
    <span class="price" style="left:589px;top:18px">$11.95</span>
  </div>

  <div class="section-title" style="top:220px">Personal Pizzas (7 inch)</div>
  <div class="section-note" style="top:247px;font-size:13px">*7 inch pizza and side salad combo for $8.25</div>

  <div class="item" style="top:314px">
    <div class="item-name">Portabella Roasted Red Pepper Pizza:</div>
    <div class="item-desc">Basil pesto, mozzarella, red peppers, portabella mushroom, baby greens and parmesan cheese …</div>
    <span class="price" style="left:598px;top:18px">$7.25</span>
  </div>

  <div class="item" style="top:364px">
    <div class="item-name">Margarita Pizza:</div>
    <div class="item-desc">Garlic infused olive oil, tomato sauce, mozzarella cheese, sliced tomatoes and pesto …</div>
    <span class="price" style="left:596px;top:18px">$6.95</span>
  </div>

  <div class="item" style="top:412px">
    <div class="item-name">BBQ Buffalo Chicken Pizza:</div>
    <div class="item-desc">BBQ sauce, mozzarella, diced celery, red onions and grilled chicken breast marinated in buttery buffalo<br>sauce drizzled with ranch dressing …</div>
    <span class="price" style="left:598px;top:37px">$7.25</span>
  </div>

  <div class="item" style="top:477px">
    <div class="item-name">Bleu Fire Chicken Pizza:</div>
    <div class="item-desc">Fire glaze, mozzarella, bleu cheese, cheddar jack, portabella mushroom, mesquite chicken,<br>scallions and cilantro …</div>
    <span class="price" style="left:592px;top:37px">$7.25</span>
  </div>

  <div class="photo photo-pizza" role="img" aria-label="Photo of a sliced personal pizza"></div>

  <div class="section-title" style="top:599px">Lunch Specials Monday - Friday 11:00am – 3:00pm</div>
  <div class="section-note" style="top:640px;font-size:15px">(No Substitutions)</div>

  <div class="item" style="top:695px">
    <div class="item-name">Chicken Ceasar Salad (Lunch portion):</div>
    <div class="item-desc">Romaine lettuce and mesquite grilled chicken, focaccia croutons, parmesan cheese and Caesar dressing …</div>
    <span class="price" style="left:589px;top:18px">$5.95</span>
  </div>

  <div class="item" style="top:750px">
    <div class="item-name">Tinga de Pollo Quesadilla &amp; House Side Salad:</div>
    <div class="item-desc">Grilled chicken is made in a cream sauce with caramelized onions, roasted peppers, smoked jalapeno,<br>cilantro and Colby jack cheese on a flour tortilla and chipotle dipping sauce …</div>
    <span class="price" style="left:593px;top:37px">$5.95</span>
  </div>

  <div class="item" style="top:828px">
    <div class="item-name">Half Grilled Sandwich Combo:</div>
    <div class="item-desc">Choose from Pastrami and Swiss on rye with mustard and sauerkraut &nbsp;- OR - &nbsp;Chicken Caprese made with<br>basil pesto, tomatoes and provolone on a French baguette. Comes with fries and house side salad…</div>
    <span class="price" style="left:593px;top:37px">$6.95</span>
  </div>

  <div class="item" style="top:905px">
    <div class="item-name">Bottomless Soup and Salad:</div>
    <div class="item-desc">Soup of the day and our house side salad made with romaine, diced tomatoes, and crumbled bleu cheese …<br>Bisque $1.00 extra)</div>
    <span class="price" style="left:589px;top:18px">$7.95 (Lobster</span>
  </div>

  <div class="photo photo-sandwich" role="img" aria-label="Photo of a grilled pastrami sandwich"></div>

  <div class="item" style="top:995px">
    <div class="item-name">Grilled Salmon Tacos:</div>
    <div class="item-desc">2 grilled Alaskan wild salmon tacos topped with pico de gallo and chipotle ranch and house side salad …</div>
    <span class="price" style="left:592px;top:18px">$5.95</span>
  </div>

  <div class="item" style="top:1054px">
    <div class="item-name">Margarita Pizza &amp; House Side Salad:</div>
    <div class="item-desc">Made with basil pesto, mozzarella, tomatoes, marinara<br>And house side salad …</div>
    <span class="price" style="left:589px;top:37px">$5.95</span>
  </div>
</body>
</html>
```